Tequila Velmaros Web Design Project

We are launching a new Ultra Premium Tequila; the brand name is "Velmaros".
Velmaros was the colloquial name given to Spanish immigrants that came to America in the 19th and early part of the 20th centuries, made fortune and went back to Spain to propel even greater opportunities for those in their homeland, started banks, built schools, roads, built eclectic houses, some acquired noble titles, they were brazen, altruist and built a better world along the way.
Our product is 100% Blue Agave and will have the 4 types of tequila: Silver, Reposado, Añejo and Extra Añejo.
Updates

Dear All,
I have attached some more information/content for your review.
Kind Regards,

After some consideration, we have decided to include our line of Premium Margaritas on the same site.
Our Margaritas are made with 100% Blue Agave Silver Tequila and lightly sweetened with Agave Nectar.
Please see file with the 5 different flavors available.
Thank you,

Target Market(s)

Our target market is affluent people, especially Hispanics, because most of the have a Spanish heritage and/or ancestry; also, entrepreneurs of today.

Industry/Entity Type

Product

Requirements
Must have
• We will provide pictures and content/text for the pages.

```html
<!DOCTYPE html>
<html lang="en">
<head>
<meta charset="utf-8">
<title>Velmaros Tequila Margarita</title>
<link rel="stylesheet" href="https://fonts.googleapis.com/css2?family=Bebas+Neue&family=Bodoni+Moda:wght@400;500&display=swap">
<style>
:root{
  --gold-deep:#d89a12;
  --gold:#efc53a;
  --cream:#f6f0dc;
  --ink:#4a1608;
  --brown:#5b1d10;
  --red:#8e1a0e;
  --maroon:#5f2b2c;
  --navy:#0c1a7a;
  --orange:#cf650f;
  --white:#ffffff;
}
*{margin:0;padding:0;box-sizing:border-box}
html,body{width:1200px;height:900px;overflow:hidden}
body{
  position:relative;
  font-family:"Bodoni Moda",serif;
  background:
    radial-gradient(ellipse 700px 420px at 240px 80px,rgba(214,120,10,.55),transparent 70%),
    linear-gradient(180deg,var(--gold-deep) 0%,var(--gold) 28%,#f2d77a 48%,var(--cream) 68%,var(--cream) 100%);
}
.abs{position:absolute}
.display{font-family:"Bebas Neue",sans-serif;color:var(--ink);line-height:1;font-weight:400}
.brand-name{left:106px;top:44px;font-size:84px;letter-spacing:2px}
.brand-line{left:106px;top:130px;font-size:62px;word-spacing:24px;letter-spacing:2px}
.brand-tier{left:106px;top:194px;font-size:32px;letter-spacing:1px}
.main-nav{left:655px;top:50px;display:flex;gap:12px;font-size:32px;letter-spacing:.5px}
.main-nav a{color:var(--ink);text-decoration:none}
.main-nav .sep{color:var(--ink)}
.shot-glass{left:646px;top:112px;width:70px;height:128px;border-radius:10px 10px 14px 14px;background:linear-gradient(180deg,#d9c05a,#c9801a 45%,#a4600e)}
.brand-story{left:830px;top:112px;width:334px;font-size:13.2px;line-height:18px;color:var(--ink)}
.rule{left:0;height:3px;width:1163px;background:var(--brown);opacity:.75}
.rule::after{content:"";position:absolute;right:0;top:-1px;width:300px;height:5px;background:var(--brown)}
.rule-top{top:260px}
.rule-mid{top:574px;left:36px;width:1127px}
.bottle{border-radius:18px 18px 10px 10px}
.bottle-silver{left:94px;top:336px;width:80px;height:182px;background:linear-gradient(90deg,#d9dde0,#ffffff 45%,#c8ccd0)}
.bottle-reposado{left:348px;top:336px;width:80px;height:182px;background:linear-gradient(90deg,#d9b06a,#f6dca4 45%,#c99a52)}
.bottle-anejo{left:808px;top:336px;width:72px;height:182px;background:linear-gradient(90deg,#b8720e,#e9a43a 45%,#9c5c08)}
.bottle-extra{left:1090px;top:338px;width:82px;height:180px;background:linear-gradient(90deg,#050505,#2a2a2a 45%,#000)}
.type-name{font-size:27px}
.type-desc{font-size:13.5px;line-height:12px;color:var(--brown)}
.silver-name{left:182px;top:340px}
.silver-desc{left:180px;top:374px}
.reposado-desc{left:250px;top:429px}
.reposado-name{left:250px;top:489px}
.anejo-name{left:884px;top:340px}
.anejo-desc{left:884px;top:375px}
.extra-desc{left:978px;top:428px}
.extra-name{left:978px;top:489px}
.hero-claim{left:500px;top:304px;width:255px;text-align:center;font-size:76px;line-height:72px;color:var(--red);letter-spacing:4px;text-shadow:2px 3px 4px rgba(0,0,0,.35)}
.margarita-panel{left:36px;top:585px;width:524px;height:253px;background:var(--maroon)}
.margarita-title{left:42px;top:10px;font-size:56px;color:var(--white);letter-spacing:10px;text-shadow:2px 3px 3px rgba(0,0,0,.5)}
.flavour{top:74px;width:36px;height:150px;border-radius:10px 10px 6px 6px}
.flavour-lime{left:33px;background:linear-gradient(#c6df6a,#8fbf2a)}
.flavour-mango{left:97px;background:linear-gradient(#f4b440,#e0800a)}
.flavour-berry{left:163px;background:linear-gradient(#f05a66,#cf1d30)}
.flavour-blue{left:227px;background:linear-gradient(#5ac6e8,#1a9acb)}
.flavour-peach{left:289px;background:linear-gradient(#f8d2c2,#ee9a86)}
.margarita-copy{left:364px;top:110px;width:140px;font-size:13px;line-height:18px;color:var(--white)}
.agave-copy{left:652px;top:596px;width:210px;font-size:13.4px;line-height:18px;color:var(--maroon)}
.agave-copy .accent{color:var(--navy)}
.photo-frame{left:893px;width:268px;height:115px;border:6px solid var(--maroon);border-radius:5px}
.photo-field{top:589px;background:linear-gradient(180deg,#9fae8a,#4f6a38)}
.photo-cellar{top:722px;background:linear-gradient(90deg,#6a4a2c,#a8886a 45%,#4a3420)}
.site-footer{left:0;top:856px;width:1200px;height:44px;background:var(--orange);color:var(--cream);font-size:12px;text-align:center;line-height:44px}
</style>
</head>
<body>
<header>
  <h1 class="abs display brand-name">Velmaros</h1>
  <p class="abs display brand-line">Tequilla Margarita</p>
  <p class="abs display brand-tier">Ultra Premium</p>
  <nav class="abs display main-nav">
    <a href="#">Home</a><span class="sep">|</span>
    <a href="#">About</a><span class="sep">|</span>
    <a href="#">Products</a><span class="sep">|</span>
    <a href="#">Contact</a>
  </nav>
  <div class="abs shot-glass" role="img" aria-label="Shot glass of golden tequila with a lime slice"></div>
  <p class="abs brand-story">Velmaros was the colloquial name given to Spanish immigrants that came to America in the 19th and early part of the 20th centuries, made fortune and went back to Spain to propel even greater opportunities for those in their homeland, started banks, built schools, roads, built eclectic houses, some acquired noble titles, they were brazen, altruist and built a better world along the way.</p>
</header>

<div class="abs rule rule-top"></div>

<section class="tequila-range">
  <div class="abs bottle bottle-silver" role="img" aria-label="Silver tequila bottle"></div>
  <h2 class="abs display type-name silver-name">Silver</h2>
  <p class="abs type-desc silver-desc">Description<br>Description-<br>Description<br>Description</p>

  <p class="abs type-desc reposado-desc">Description<br>Description-<br>Description<br>Description</p>
  <h2 class="abs display type-name reposado-name">Reposado</h2>
  <div class="abs bottle bottle-reposado" role="img" aria-label="Reposado tequila bottle"></div>

  <p class="abs display hero-claim">Ultra Premium Tequilla</p>

  <div class="abs bottle bottle-anejo" role="img" aria-label="Añejo tequila bottle"></div>
  <h2 class="abs display type-name anejo-name">Anejo</h2>
  <p class="abs type-desc anejo-desc">Description<br>Description-<br>Description<br>Description</p>

  <p class="abs type-desc extra-desc">Description<br>Description-<br>Description<br>Description</p>
  <h2 class="abs display type-name extra-name">Extranejo</h2>
  <div class="abs bottle bottle-extra" role="img" aria-label="Extra añejo tequila bottle"></div>
</section>

<div class="abs rule rule-mid"></div>

<section class="abs margarita-panel">
  <h2 class="abs display margarita-title">Margaritas</h2>
  <div class="abs flavour flavour-lime" role="img" aria-label="Lime margarita bottle"></div>
  <div class="abs flavour flavour-mango" role="img" aria-label="Mango margarita bottle"></div>
  <div class="abs flavour flavour-berry" role="img" aria-label="Strawberry margarita bottle"></div>
  <div class="abs flavour flavour-blue" role="img" aria-label="Blueberry margarita bottle"></div>
  <div class="abs flavour flavour-peach" role="img" aria-label="Grapefruit margarita bottle"></div>
  <p class="abs margarita-copy">Loren ipsum&nbsp; Loren ipsum Loren ipsum Loren ipsum Loren ipsum Loren ipsum Loren ipsum Loren ipsum Loren ipsum</p>
</section>

<section class="abs agave-copy">
  <p>Made of <span class="accent">100% Blue Agave</span><br>
  Lorem ipsum&nbsp; Lorem ipsum<br>Lorem ipsum Lorem ipsum<br>Lorem ipsum Lorem ipsum<br>Lorem ipsum Lorem ipsum<br>Lorem ipsum Lorem ipsum<br>Lorem ipsum Lorem ipsum<br>Lorem ipsum Lorem ipsum<br>Lorem ipsum Lorem ipsum<br>Lorem ipsum Lorem ipsum<br>Lorem ipsum Lorem ipsum<br>Lorem ipsum Lorem ipsum<br>Lorem ipsum Lorem ipsum</p>
</section>

<div class="abs photo-frame photo-field" role="img" aria-label="Photo of a blue agave field"></div>
<div class="abs photo-frame photo-cellar" role="img" aria-label="Photo of a tequila tasting among aging barrels"></div>

<footer class="abs site-footer">copyright 2012</footer>
</body>
</html>
```